Whitcombe Legal Group Promo Flyers

** I've increased the payment for this job is hopes of getting some more sophisticated design options. See feedback on current designs for guidance. I want this to be sophisticated, elegant, effective design. Please stay away from the brown/blue color palate that has been used in so many of these design options. It's not working. I'd love to see richer, deeper colors with more dimension. **

The Whitcombe Legal Group is trying to market itself as a law firm that is different than other firms. They listen to clients, meet their guidelines, provide excellent communication and will even start work for free to showcase their expertise. I need three separate flyers that will primarily be used as PDFs, but may on occasion be printed.

We're looking for a clean look.

I've attached two sample infographics that are pieces done by another company in the industry. We like that look (sizes of those are different, but the overall look is good).

Target Market(s)

Insurance companies and corporate executives who buy legal services to help them manage their book of litigation. Typical buyer is in 40s to 50s. Fairly racially diverse.

Industry/Entity Type

Communication

Requirements
Must have
• Each document will be a one-page PDF that can be easily emailed to potential clients. Must be one side only for each.

One flyer each for these three files, which are included:
Whitcombe firm by the numbers
Whitcombe firm client advantage program
Whitc firm overview

Must use firm logo. Contact information should pop.

"Topping the list" piece is an inforgraphic that should really focus on bold use of the numbers or text in blue. Mix up the page and make it fun and interesting.

Logo colors are:

Brown: R: 101 G: 50 B:27, HEX: 65321B

Grey: R:129 G: 145 B:144, HEX: 819190
Nice to have
• Firm website is very dull and uninteresting. These pieces need to pop more than past pieces.

http://www.whitcombelegalgroup-example.com/
Should not have
• No stock photos of people in groups (all law firms use those and they are boring and overdone).

```html
<!DOCTYPE html>
<html lang="en">
<head>
<meta charset="utf-8">
<title>Whitcombe Legal Group – Flyer</title>
<link href="https://fonts.googleapis.com/css2?family=Mulish:wght@400;600;700;800&display=swap" rel="stylesheet">
<style>
  :root{
    --stage:#e4e2ea;
    --purple-deep:#4b2f8f;
    --purple:#6346ad;
    --purple-mid:#7457bd;
    --purple-light:#8a70cc;
    --white:#ffffff;
    --grey:#819190;
    --ink:#2c2350;
    --photo-dark:#6b3d22;
    --photo-mid:#b27a4c;
    --photo-light:#e8ddd4;
  }
  *{box-sizing:border-box;margin:0;padding:0}
  html,body{width:1200px;height:750px;overflow:hidden}
  body{background:var(--stage);font-family:"Mulish",sans-serif;color:var(--white);position:relative}

  .flyer{position:absolute;left:344px;top:20px;width:512px;height:710px;background:var(--purple);overflow:hidden;box-shadow:0 10px 30px rgba(40,20,80,.25)}

  .hero-photo{position:absolute;left:0;top:0;width:512px;height:340px;
    background:radial-gradient(ellipse at 30% 55%,var(--photo-mid) 0%,var(--photo-dark) 45%,transparent 70%),
               linear-gradient(120deg,#d9c9bd 0%,var(--photo-light) 45%,#c9b4a6 70%,#9e8a9e 100%)}
  .steps{position:absolute;left:0;top:0}

  .brand{position:absolute;right:0;top:22px;width:192px;height:62px;background:var(--white);display:flex;align-items:center;gap:8px;padding-left:14px}
  .brand-square{width:10px;height:10px;background:var(--purple-deep)}
  .brand-name{font-weight:700;color:var(--purple-deep);font-size:15px;line-height:1.15}

  .badge{position:absolute;left:290px;top:112px;width:172px;height:172px;border-radius:50%;background:var(--white);display:flex;flex-direction:column;align-items:center;justify-content:center;text-align:center;color:var(--purple-deep)}
  .badge::after{content:"";position:absolute;inset:8px;border:2px dashed var(--purple-deep);border-radius:50%}
  .badge-stars{width:48px;height:15px;margin-bottom:6px}
  .badge-lead{font-size:8.4px;font-weight:800;letter-spacing:.2px}
  .badge-main{font-size:12.5px;font-weight:800;line-height:1.2;margin-top:2px}

  .col{position:absolute;font-size:7.8px;line-height:1.33;text-align:justify}
  .col h3{font-size:9.6px;font-weight:700;line-height:1.15;text-align:left;margin-bottom:1px}
  .col p{margin-bottom:5px}

  .col-intro{left:0;top:324px;width:172px;bottom:47px;background:var(--purple-deep);padding:12px 10px 0 16px}
  .col-intro::before{content:"";position:absolute;left:8px;top:30px;width:2px;height:84px;background:var(--white)}
  .col-metrics{left:172px;top:300px;width:170px;bottom:47px;background:var(--purple-mid);padding:6px 10px 0}

  .practice{position:absolute;left:350px;top:330px;width:156px}
  .practice h2{font-size:17px;font-weight:600;margin-bottom:9px}
  .practice ul{list-style:none}
  .practice li{display:flex;gap:5px;font-size:8.6px;font-weight:700;line-height:1.27;margin-bottom:8px}
  .tick{flex:0 0 11px;height:11px;margin-top:1px}

  .find{position:absolute;left:376px;top:548px;width:96px;height:18px;border-radius:9px;background:var(--white);color:var(--purple-deep);font-size:8px;font-weight:700;display:flex;align-items:center;justify-content:center;gap:6px}
  .contacts{position:absolute;right:14px;top:576px;list-style:none;text-align:right}
  .contacts li{display:flex;align-items:center;justify-content:flex-end;gap:6px;font-size:7.2px;margin-bottom:6px}
  .dot{width:10px;height:10px;border-radius:50%;background:var(--white)}

  .footer{position:absolute;left:0;right:0;bottom:0;height:47px;background:var(--white);display:flex;align-items:center;color:var(--ink);padding:0 12px 0 10px}
  .footer-brand{display:flex;align-items:center;gap:5px;padding-right:8px;border-right:1px solid var(--grey);height:32px}
  .footer-brand .brand-square{width:6px;height:6px}
  .footer-brand .brand-name{font-size:8px}
  .footer-address{padding-left:10px;flex:1}
  .footer-address strong{display:block;font-size:9.5px;font-weight:800}
  .footer-address span{font-size:5.6px}
  .footer-phone{font-size:8.4px;font-weight:800;border-left:1px solid var(--grey);padding-left:8px}
</style>
</head>
<body>
<main class="flyer">
  <div class="hero-photo" role="img" aria-label="Close-up photo of a wooden judge's gavel resting on its block beside rolled parchment"></div>

  <svg class="steps" width="512" height="345" viewBox="0 0 512 345" aria-hidden="true">
    <polygon fill="var(--purple-light)" opacity=".75" points="190,345 190,330 210,330 210,318 230,318 230,306 250,306 250,294 270,294 270,282 290,282 290,270 512,170 512,345"/>
    <polygon fill="var(--purple)" points="0,345 0,324 172,324 172,300 240,300 240,288 260,288 260,276 280,276 280,264 512,264 512,345"/>
    <polygon fill="var(--purple)" points="440,264 440,240 455,240 455,220 470,220 470,200 485,200 485,180 500,180 500,160 512,160 512,264"/>
  </svg>

  <div class="brand">
    <span class="brand-square"></span>
    <span class="brand-name">Whitcombe<br>Legal Group</span>
  </div>

  <div class="badge">
    <svg class="badge-stars" viewBox="0 0 46 14" aria-hidden="true">
      <g fill="var(--purple-deep)">
        <polygon points="7,0 8.8,4.8 14,5 10,8.3 11.3,13.5 7,10.6 2.7,13.5 4,8.3 0,5 5.2,4.8"/>
        <polygon transform="translate(16 0)" points="7,0 8.8,4.8 14,5 10,8.3 11.3,13.5 7,10.6 2.7,13.5 4,8.3 0,5 5.2,4.8"/>
        <polygon transform="translate(32 0)" points="7,0 8.8,4.8 14,5 10,8.3 11.3,13.5 7,10.6 2.7,13.5 4,8.3 0,5 5.2,4.8"/>
      </g>
    </svg>
    <div class="badge-lead">WE ARE TRIAL LAWYERS</div>
    <div class="badge-main">FOR BUSINESS,<br>PROFESSIONALS<br>AND<br>ENTREPRENEURS</div>
  </div>

  <section class="col col-intro">
    <h3>Clients Come First</h3>
    <p>Clients come first at The Whitcombe Legal Group. Our extremely well-credentialed attorneys know that clients want more than legal expertise — they want partners who understand that communication and process during the management of a case are just as important as the outcome. They want advice and guidance. They want a true business partner.</p>
    <h3>Great Outcomes, Great Process Great Communication</h3>
    <p>A good attorney will get you the desired outcome on a case. A great attorney will do the same while following your process and keeping your informed along the way — all while being mindful of the established budget. We work closely with our clients to understand their litigation management guidelines and we ensure that we follow them. We know that our clients have their own internal reporting structures and timeframes and we strive to provide the work product and communication so those reporting requirements can be met.</p>
  </section>

  <section class="col col-metrics">
    <h3>Metrics That Matter</h3>
    <p>Providing excellent legal counsel today also means being able to provide clients with the data they need to evaluate performance. While we're managing the details of each case, we're also keeping track of the big picture so we can report metrics back to our clients. Cycle time, cost, quality and predictability are just some of the metrics we track. We work with each client to ensure we have the data they desire. We understand and embrace the importance of business process.</p>
    <h3>Expertise No One Else Has</h3>
    <p>Our attorneys bring unique expertise to managing our clients' litigation. For example, we excel at transportation and construction cases because one of our partners, Dan Marlowe, ran a trucking company, and then was responsible for maintaining mining machines on the Deep Tunnel project in Chicago. Another partner, Tom Whitcombe, has deep knowledge of emergency litigation. We've literally been in the trenches sharing your business &amp; life experiences. Each of our attorneys brings unique perspectives to each of the Firm's practice areas.</p>
  </section>

  <section class="practice">
    <h2>Practice Areas</h2>
    <ul>
      <li><svg class="tick" viewBox="0 0 12 12" aria-hidden="true"><circle cx="6" cy="6" r="6" fill="var(--white)"/><path d="M3.2 6.2 5.2 8.1 8.9 4" fill="none" stroke="var(--purple)" stroke-width="1.6"/></svg><span>Insurance (coverage, defense, subrogation, risk managing, program administration)</span></li>
      <li><svg class="tick" viewBox="0 0 12 12" aria-hidden="true"><circle cx="6" cy="6" r="6" fill="var(--white)"/><path d="M3.2 6.2 5.2 8.1 8.9 4" fill="none" stroke="var(--purple)" stroke-width="1.6"/></svg><span>Professional Liability (attorneys, accountants, D &amp; O, E &amp; O, EPL)</span></li>
      <li><svg class="tick" viewBox="0 0 12 12" aria-hidden="true"><circle cx="6" cy="6" r="6" fill="var(--white)"/><path d="M3.2 6.2 5.2 8.1 8.9 4" fill="none" stroke="var(--purple)" stroke-width="1.6"/></svg><span>Business Litigation (emergencies, injunctions, contract, partners, shareholders, employees, property, trade secrets, restrictive covenants, banking, finance)</span></li>
      <li><svg class="tick" viewBox="0 0 12 12" aria-hidden="true"><circle cx="6" cy="6" r="6" fill="var(--white)"/><path d="M3.2 6.2 5.2 8.1 8.9 4" fill="none" stroke="var(--purple)" stroke-width="1.6"/></svg><span>Construction</span></li>
      <li><svg class="tick" viewBox="0 0 12 12" aria-hidden="true"><circle cx="6" cy="6" r="6" fill="var(--white)"/><path d="M3.2 6.2 5.2 8.1 8.9 4" fill="none" stroke="var(--purple)" stroke-width="1.6"/></svg><span>Commercial Transportation</span></li>
    </ul>
  </section>

  <div class="find">Find us :
    <svg width="10" height="10" viewBox="0 0 10 10" aria-hidden="true"><circle cx="4" cy="4" r="3" fill="none" stroke="var(--purple-deep)" stroke-width="1.5"/><line x1="6.2" y1="6.2" x2="9.3" y2="9.3" stroke="var(--purple-deep)" stroke-width="1.6"/></svg>
  </div>
  <ul class="contacts">
    <li>www.social-example.com/whitcombe <span class="dot"></span></li>
    <li>www.micro-example.com/whitcombelegal <span class="dot"></span></li>
    <li>www.whitcombelegalgroup-example.com <span class="dot"></span></li>
  </ul>

  <footer class="footer">
    <div class="footer-brand">
      <span class="brand-square"></span>
      <span class="brand-name">Whitcombe<br>Legal Group</span>
    </div>
    <div class="footer-address">
      <strong>The Whitcombe Legal Group</strong>
      <span>400 W. Harlow Ave. Suite 1200 Chicago, Illinois 60600, United States.</span>
    </div>
    <div class="footer-phone">Phone : (555) 010 2200 &nbsp;|&nbsp; Fax : (555) 010 2201</div>
  </footer>
</main>
</body>
</html>
```